Moon River Healing Buisness Cards

I am looking to create a business card for a healing business. In the business I provide coaching and Reiki. I am a licensed LCPC (licensed clinical professional counselor)

Moon River Healing
Soul Centered Healing, Reiki Healinig

Lena Vasquez, L.C.P.C

The card should include the following
biz name: Moon River Healing
my name: Lena Vasquez
website: Lenavasquez.example
email: lena.dorwin@mailbox.example
instagram handle: lenadorwinvasquez

Target Market(s)

Women ages 25-65

```html
<!DOCTYPE html>
<html lang="en">
<head>
<meta charset="utf-8">
<title>Moon River Healing – Business Cards</title>
<link href="https://fonts.googleapis.com/css2?family=Lato:wght@400&display=swap" rel="stylesheet">
<style>
  :root {
    --backdrop: #2b2b2b;
    --card-dark: #262626;
    --card-light: #f4f4f2;
    --ink-light: #ffffff;
    --ink-dark: #3c3c3c;
    --accent-blue: #5b83c4;
    --accent-green: #9cc26a;
  }
  html, body {
    margin: 0;
    width: 1200px;
    height: 900px;
    overflow: hidden;
    background: var(--backdrop);
    font-family: 'Lato', Arial, sans-serif;
  }
  .canvas {
    position: relative;
    width: 1200px;
    height: 900px;
  }
  .card {
    position: absolute;
    width: 500px;
    height: 286px;
    border-radius: 22px;
    box-shadow: 0 14px 30px rgba(0,0,0,0.45);
  }
  .card--front {
    left: 70px;
    top: 120px;
    background: var(--card-dark);
  }
  .card--back {
    left: 630px;
    top: 120px;
    background: var(--card-light);
  }
  .brand {
    display: flex;
    align-items: center;
    gap: 14px;
    font-weight: 400;
    line-height: 1.1;
  }
  .brand__dot {
    border-radius: 50%;
    background: var(--accent-green);
    flex: none;
  }
  .card--front .brand {
    position: absolute;
    left: 0; right: 0; top: 118px;
    justify-content: center;
    font-size: 32px;
    color: var(--ink-light);
    white-space: nowrap;
  }
  .card--front .brand__dot {
    width: 34px;
    height: 34px;
  }
  .card--back .brand {
    position: absolute;
    left: 40px;
    top: 150px;
    width: 170px;
    gap: 12px;
    font-size: 22px;
    color: var(--ink-dark);
  }
  .card--back .brand__dot {
    width: 30px;
    height: 30px;
  }
  .contact {
    position: absolute;
    left: 258px;
    top: 62px;
    color: var(--ink-dark);
  }
  .contact__name {
    margin: 0 0 14px;
    font-size: 24px;
    font-weight: 400;
  }
  .contact__list {
    list-style: none;
    margin: 0;
    padding: 0;
    font-size: 12px;
  }
  .contact__list li {
    display: flex;
    align-items: center;
    gap: 8px;
    margin-bottom: 8px;
    white-space: nowrap;
  }
  .contact__icon {
    width: 12px;
    height: 12px;
    flex: none;
  }
  .showcase-brand {
    position: absolute;
    left: 70px;
    top: 620px;
    gap: 18px;
    font-size: 52px;
    color: var(--ink-light);
    white-space: nowrap;
  }
  .showcase-brand .brand__dot {
    width: 48px;
    height: 48px;
  }
</style>
</head>
<body>
<main class="canvas">
  <section class="card card--front" aria-label="Card front">
    <div class="brand"><span class="brand__dot"></span>Moon River Healing</div>
  </section>

  <section class="card card--back" aria-label="Card back">
    <div class="brand"><span class="brand__dot"></span><span>Moon River<br>Healing</span></div>
    <div class="contact">
      <h2 class="contact__name">Lena Vasquez</h2>
      <ul class="contact__list">
        <li>
          <svg class="contact__icon" viewBox="0 0 12 12" aria-hidden="true">
            <circle cx="6" cy="6" r="5" fill="none" stroke="#5b83c4" stroke-width="1.2"/>
            <ellipse cx="6" cy="6" rx="2.2" ry="5" fill="none" stroke="#5b83c4" stroke-width="1"/>
            <line x1="1" y1="6" x2="11" y2="6" stroke="#5b83c4" stroke-width="1"/>
          </svg>
          Lenavasquez.example
        </li>
        <li>
          <svg class="contact__icon" viewBox="0 0 12 12" aria-hidden="true">
            <rect x="0.5" y="2.5" width="11" height="7.5" fill="#5b83c4"/>
            <polyline points="0.8,3 6,7 11.2,3" fill="none" stroke="#fff" stroke-width="1"/>
          </svg>
          lena.dorwin@mailbox.example
        </li>
        <li>
          <svg class="contact__icon" viewBox="0 0 12 12" aria-hidden="true">
            <rect x="1" y="1" width="10" height="10" fill="#5b83c4"/>
          </svg>
          lenadorwinvasquez
        </li>
      </ul>
    </div>
  </section>

  <div class="brand showcase-brand"><span class="brand__dot"></span>Moon River Healing</div>
</main>
</body>
</html>
```